Company identity deisgn should support 2 languages

I would like to get our company identity design
This includes the following only
Business Cards 2 languages Arabic and English
Email signature
Letterhead
Linkedin profile images
Attached is the logo in Ai format

Requirements
Must have
• For business card
Must have
Name and Adrees in arabic
Name and Address in english
You might use both side of the card
Should not have
• Any pictures other than the logo

```html
<!DOCTYPE html>
<html lang="en">
<head>
<meta charset="utf-8">
<title>Nova Cortex Systems – Business Card</title>
<link href="https://fonts.googleapis.com/css2?family=Roboto:wght@400;500;700&family=Noto+Kufi+Arabic:wght@400&display=swap" rel="stylesheet">
<style>
  :root{
    --backdrop:#2b2b2d;
    --card:#ffffff;
    --brand-blue:#1e86d0;
    --band-blue:#1b7fcc;
    --text-grey:#6f6f72;
    --light-grey:#a9a9ad;
    --white:#ffffff;
  }
  *{margin:0;padding:0;box-sizing:border-box}
  html,body{width:1200px;height:929px;overflow:hidden;background:var(--backdrop)}
  .card{
    position:absolute;left:100px;top:179px;width:1000px;height:571px;
    background:var(--card);overflow:hidden;
    box-shadow:0 18px 40px rgba(0,0,0,.45);
    font-family:"Roboto",sans-serif;
  }
  .brand{position:absolute;left:330px;top:82px;display:flex;align-items:center;gap:16px}
  .brand-dot{width:58px;height:58px;border-radius:50%;background:var(--brand-blue)}
  .brand-text{display:flex;flex-direction:column}
  .brand-name{font-size:34px;font-weight:500;color:var(--brand-blue);letter-spacing:1px;text-transform:uppercase}
  .brand-rule{height:2px;background:var(--brand-blue);margin:6px 0 6px;width:100%}
  .brand-arabic{font-family:"Noto Kufi Arabic",sans-serif;font-size:15px;color:var(--light-grey);direction:rtl;text-align:right;letter-spacing:2px}

  .person{position:absolute;left:150px;top:255px}
  .person-name{font-size:36px;font-weight:700;color:var(--brand-blue);white-space:nowrap}
  .person-name .ar{font-family:"Noto Kufi Arabic",sans-serif;font-weight:400;font-size:32px}
  .person-title{font-size:26px;font-weight:500;color:var(--text-grey);margin-top:2px}
  .contacts{list-style:none;margin-top:26px}
  .contacts li{display:flex;align-items:center;gap:14px;font-size:26px;color:var(--text-grey);height:38px}
  .contacts svg{width:24px;height:24px;flex:none}

  .address-ar{
    position:absolute;right:70px;top:230px;width:360px;
    font-family:"Noto Kufi Arabic",sans-serif;font-size:25px;line-height:1.55;
    color:var(--text-grey);direction:rtl;text-align:right;
  }
  .band{
    position:absolute;left:0;bottom:0;width:100%;height:88px;
    background:linear-gradient(90deg,var(--band-blue),#2590d6);
    display:flex;align-items:center;padding-left:250px;
  }
  .band-text{font-size:31px;font-weight:500;color:var(--white);white-space:nowrap}
</style>
</head>
<body>
  <section class="card">
    <header class="brand">
      <span class="brand-dot"></span>
      <div class="brand-text">
        <span class="brand-name">Nova Cortex Systems</span>
        <span class="brand-rule"></span>
        <span class="brand-arabic">شركة نوفا كورتكس للأنظمة</span>
      </div>
    </header>

    <div class="person">
      <h1 class="person-name">Samir Haddad <span class="ar">(سمير حداد)</span></h1>
      <p class="person-title">Business Development Director</p>
      <ul class="contacts">
        <li>
          <svg viewBox="0 0 24 24" aria-hidden="true"><path fill="#1e86d0" d="M6.6 10.8a15.1 15.1 0 0 0 6.6 6.6l2.2-2.2a1 1 0 0 1 1-.25 11.4 11.4 0 0 0 3.6.57 1 1 0 0 1 1 1V20a1 1 0 0 1-1 1A17 17 0 0 1 3 4a1 1 0 0 1 1-1h3.5a1 1 0 0 1 1 1c0 1.25.2 2.45.57 3.57a1 1 0 0 1-.25 1z"/></svg>
          +96 6500 123 456
        </li>
        <li>
          <svg viewBox="0 0 24 24" aria-hidden="true"><rect x="2" y="5" width="20" height="14" fill="#1e86d0"/><path d="M2 5l10 8 10-8" fill="none" stroke="#fff" stroke-width="1.6"/></svg>
          hello@novacortex.com
        </li>
        <li>
          <svg viewBox="0 0 24 24" aria-hidden="true"><circle cx="12" cy="12" r="10" fill="#1e86d0"/><path d="M2 12h20M12 2c3 3 3 17 0 20M12 2c-3 3-3 17 0 20" fill="none" stroke="#fff" stroke-width="1.4"/></svg>
          www.novacortex.com
        </li>
      </ul>
    </div>

    <address class="address-ar">
      برج النخيل الدور 12<br>
      شارع الحديقة<br>
      مدينة النور
    </address>

    <footer class="band">
      <span class="band-text">Palm tower 12th floor Garden st. Al Noor City</span>
    </footer>
  </section>
</body>
</html>
```